****Business Card Design for Cormwell Development. Design based around attached logo/company name

I’m looking for business card design for my company Cormwell Development Group,LLC. Design should be professional, sharp and minimal. Outside of the attached logos, greyscale colors for remainder of cards. My thoughts are two-sided card with attached logo on one side and my info on the other but open to one-sided as well with right design.
Target Market(s)
Real estate professionals including banks, private investors, property owners, developers, commercial tenants like Brewlantic, Granvey or Tamsett’s.
Industry/Entity Type
Commercial real estate development and investments.
Contact Information for Business Card
Name, title, email, phone #’s, web address and physical address
Font styles to use
Other font styles liked:
- Helvetica, Garamond, etc
Colors
Designer to choose only greyscale colors for use in the design.
Requirements
Must have
- Attached logo first or second options.
Nice to have
- Two sided card with logo on one side. Attached Logo/company name can be laid out any way that flows as long as it’s legible.name
Should not have
- No loud colors. ***Please do not include logo, I have removed the company design with a logo image.

```html
<!DOCTYPE html>
<html lang="en">
<head>
<meta charset="utf-8">
<title>Cormwell Development Group, LLC – Business Card</title>
<link href="https://fonts.googleapis.com/css2?family=Cinzel:wght@400;700&family=Arimo:wght@400&display=swap" rel="stylesheet">
<style>
  :root {
    --page: #1a1a1a;
    --card: #232323;
    --card-edge: #2c2c2c;
    --ink: #f2f2f2;
    --silver: #c4c4c4;
    --label: #8a8a94;
    --rule: #d8d8d8;
  }
  * { box-sizing: border-box; margin: 0; padding: 0; }
  html, body {
    width: 1200px; height: 900px; overflow: hidden;
    background: var(--page);
  }
  .sheet {
    width: 1200px; height: 900px;
    display: flex; flex-direction: column; align-items: center; justify-content: center;
    gap: 40px;
  }
  .card {
    position: relative;
    width: 700px; height: 400px;
    background: var(--card);
    border: 1px solid var(--card-edge);
  }
  /* Front */
  .card-front {
    display: flex; align-items: center; justify-content: center;
  }
  .front-name {
    font-family: "Cinzel", serif;
    font-weight: 400;
    font-size: 40px;
    letter-spacing: 6px;
    color: var(--silver);
  }
  /* Back */
  .card-back { padding: 44px 56px; }
  .wordmark {
    font-family: "Cinzel", serif;
    font-weight: 400;
    color: var(--ink);
    line-height: 1;
  }
  .wordmark-main { display: block; font-size: 34px; letter-spacing: 2px; }
  .wordmark-sub {
    display: block; font-size: 13px; letter-spacing: 2.5px;
    border-top: 1px solid var(--rule); margin-top: 6px; padding-top: 5px;
    width: 318px;
  }
  .person { margin-top: 34px; }
  .person-name {
    font-family: "Cinzel", serif; font-weight: 700;
    font-size: 22px; letter-spacing: 3px; color: var(--ink);
  }
  .person-title {
    font-family: "Arimo", sans-serif; font-size: 16px; color: var(--ink); margin-top: 2px;
  }
  .details {
    font-family: "Arimo", sans-serif; font-size: 17px; color: var(--ink);
    line-height: 1.3; margin-top: 22px;
  }
  .details p + p.gap { margin-top: 16px; }
  .label { color: var(--label); }
  .cell {
    position: absolute; right: 40px; bottom: 32px;
    font-family: "Arimo", sans-serif; font-size: 17px; color: var(--ink);
  }
</style>
</head>
<body>
<main class="sheet">
  <section class="card card-front" aria-label="Card front">
    <span class="front-name">CORMWELL</span>
  </section>

  <section class="card card-back" aria-label="Card back">
    <h1 class="wordmark">
      <span class="wordmark-main">CORMWELL</span>
      <span class="wordmark-sub">DEVELOPMENT GROUP, LLC</span>
    </h1>
    <div class="person">
      <h2 class="person-name">DANIEL HARLOW</h2>
      <p class="person-title">Director</p>
    </div>
    <div class="details">
      <p><span class="label">Address:</span> 1187 Ridgeway<br>Lane Salem, OR 97301</p>
      <p class="gap"><span class="label">Email:</span> info@cormwellgroup.com</p>
      <p><span class="label">Web:</span> www.cormwellgroup.com</p>
    </div>
    <p class="cell"><span class="label">Cell:</span> (555) 014-2290</p>
  </section>
</main>
</body>
</html>
```